PowerPoint template design needed for sales and presales presentations

We would like to have a bright and light, contemporary PowerPoint design based on our existing style assets (see attached files).
We are based in Latvia. Our business is ERP systems implementation, IT infrastructure building and supporting our customers. We are moving from traditional Add-hoc projects model to standardized flat-rate offerings. Our technology platform is Quintavel.
The value proposition of our offerings is based around simplicity, transparency, quality, peace of mind, trust, easy of doing business.
I have to add that if any special are being used, they must be unicode to ensure proper Latvian language characters display.
Updates
Hi! The reason is an error at your side. Today it's 24/08/2020 when I started the project and made a payment. Still for some funny reason in the BRIEF I see that the project deadline is set to 20/08/2020. No wonder no designers are applying...
Target Market(s)
Small and medium enterprise
Look and feel

```html
<!DOCTYPE html>
<html lang="en">
<head>
<meta charset="utf-8">
<title>Nordal Works – Presentation Template</title>
<link href="https://fonts.googleapis.com/css2?family=Oswald:wght@400;500&family=Montserrat:wght@500;700&family=Open+Sans:wght@400;600;700&display=swap" rel="stylesheet">
<style>
:root{
  --black:#0b0b0c;
  --ink:#222428;
  --grey-text:#6b6e73;
  --rail:#d9dadc;
  --green:#8dc63f;
  --teal:#13b9b5;
  --yellow:#fcd000;
  --red:#d7262b;
  --olive:#b88f00;
  --slate:#2e3440;
  --violet:#6a3d8f;
  --magenta:#b0217a;
  --row-grey:#c9cacc;
  --paper:#ffffff;
}
*{box-sizing:border-box;margin:0;padding:0}
html,body{width:1160px;height:1200px;overflow:hidden;background:var(--paper)}
body{position:relative;font-family:"Open Sans",Arial,sans-serif;color:var(--ink)}
.slide{position:absolute;width:356px;height:200px;background:var(--paper);overflow:hidden;box-shadow:0 1px 4px rgba(0,0,0,.22)}
.col-1{left:22px}.col-2{left:401px}.col-3{left:783px}
.row-1{top:49px}.row-2{top:282px}.row-3{top:518px}.row-4{top:748px}.row-5{top:979px}

/* side rail */
.rail{position:absolute;left:0;top:0;width:12px;height:100%;background:var(--rail)}
.tab{position:absolute;left:0;width:12px;height:10px;color:#fff;font:700 4.5px/10px "Open Sans",sans-serif;padding-left:3px;white-space:nowrap;letter-spacing:.4px}
.tab.active{width:52px}
.tab .label{position:absolute;left:18px;font-size:4px;letter-spacing:.8px}
.t1{top:22px}.t2{top:33.5px}.t3{top:45px}.t4{top:56.5px}.t5{top:68px}.t6{top:79.5px}.t7{top:91px}
.c-black{background:var(--black)}.c-green{background:var(--green)}.c-teal{background:var(--teal)}
.c-yellow{background:var(--yellow)}.c-red{background:var(--red)}.c-olive{background:var(--olive)}
.c-slate{background:var(--slate)}.c-violet{background:var(--violet)}.c-magenta{background:var(--magenta)}

/* brand */
.brand{position:absolute;display:flex;align-items:center;gap:3px;font:700 5px/1 "Montserrat",sans-serif;color:var(--ink);letter-spacing:.3px}
.brand .mark{width:10px;height:10px;border:1px solid var(--ink)}
.brand.small{right:10px;top:8px}
.brand.large{left:17px;top:23px;font-size:9px;gap:5px}
.brand.large .mark{width:20px;height:20px;border-width:1.5px}

.heading{position:absolute;font:400 11px/1.15 "Oswald",sans-serif;color:var(--ink);text-transform:uppercase}
.heading::before{content:"";position:absolute;left:0;top:-7px;width:14px;height:1px;background:var(--ink)}
.body{position:absolute;font-size:4px;line-height:1.45;color:var(--grey-text)}
.lead{position:absolute;font-size:5px;line-height:1.45;color:var(--grey-text)}

.pager{position:absolute;right:8px;bottom:6px;display:flex;align-items:center;gap:3px;font:600 5px/1 "Open Sans",sans-serif;color:var(--ink)}
.pager i{width:6px;height:6px;border-radius:50%;background:#d0d1d3;display:block}

.art{position:absolute}

/* title slide */
.cover-title{position:absolute;left:17px;top:102px;font:700 11.5px/1.25 "Montserrat",sans-serif;color:var(--black)}
.cover-sub{position:absolute;left:17px;top:134px;font:500 7px/1 "Montserrat",sans-serif;color:var(--black)}
.cover-date{position:absolute;left:17px;top:178px;font-size:4.5px;color:var(--ink)}

/* contents */
.toc{position:absolute;left:74px;top:58px;width:230px;list-style:none}
.toc li{display:flex;font-size:4.5px;color:var(--grey-text);height:14.3px;align-items:center}
.toc .n{width:9px}
.toc .dots{flex:1;border-bottom:1px dotted #9a9ca0;margin:0 3px;transform:translateY(1px)}

/* stat band */
.stat-band{position:absolute;left:12px;top:130px;width:344px;height:45px;background:linear-gradient(90deg,var(--teal),var(--green) 70%)}
.stat-num{position:absolute;left:52px;top:137px;font:700 22px/1 "Montserrat",sans-serif;color:#fff}
.stat-num sup{font-size:12px}
.stat-text{position:absolute;left:103px;top:140px;width:100px;font-size:4px;line-height:1.4;color:#fff}

/* timeline */
.tl-line{position:absolute;left:178px;top:12px;width:1px;height:180px;background:var(--ink)}
.tl-year{position:absolute;font:500 5px/1 "Oswald",sans-serif}
.tl-text{position:absolute;width:66px;font-size:3.6px;line-height:1.4;color:var(--grey-text)}
.tl-text.r{text-align:right}

/* sections */
.section{color:#fff}
.section .sec-title{position:absolute;left:34px;top:118px;font:500 20px/1 "Oswald",sans-serif;letter-spacing:.3px}
.section .sec-text{position:absolute;left:34px;top:145px;width:150px;font-size:3.8px;line-height:1.4;font-weight:600}
.bg-black{background:var(--black)}.bg-green{background:var(--green)}.bg-teal{background:var(--teal)}

/* services */
.service{position:absolute;width:120px;height:26px}
.service .icon{position:absolute;left:0;top:0;width:24px;height:24px;display:flex;align-items:center;justify-content:center}
.service .name{position:absolute;left:28px;top:0;font-size:6px;color:var(--ink)}
.service .txt{position:absolute;left:28px;top:8px;width:88px;font-size:3.5px;line-height:1.4;color:var(--grey-text)}

/* team */
.portrait{position:absolute;width:46px;height:46px;background:linear-gradient(160deg,#e9edf1,#c7cdd4)}
.member{position:absolute;width:56px;text-align:center}
.member .who{font:500 4.6px/1 "Oswald",sans-serif;color:var(--teal)}
.member .role{font-size:3.6px;color:var(--grey-text);margin-top:1px}
.member .bio{font-size:3.4px;line-height:1.4;color:var(--grey-text);margin-top:4px;text-align:justify}

/* tables */
table{position:absolute;border-collapse:collapse;font-size:3.6px;color:#5b5e63}
.orders{left:95px;top:73px;width:252px}
.orders th{background:var(--green);color:#fff;font:500 5px/15px "Oswald",sans-serif;text-transform:uppercase}
.orders td{height:15.7px;text-align:center}
.orders tr:nth-child(odd) td{background:var(--row-grey)}
.ledger{left:74px;top:68px;width:242px}
.ledger th{background:var(--green);color:#fff;font:700 5px/12px "Open Sans",sans-serif;text-align:left;padding-left:3px;border-right:1px solid #fff}
.ledger td{height:9.8px;border-bottom:1px solid #2b2d31;padding-left:3px}
.ledger td.v{text-align:center;color:var(--ink)}
.ledger td.in{padding-left:16px}
.ledger tr.total td{background:var(--black);color:#fff;font-weight:700;border-right:1px solid #444}

/* closing */
.thanks{position:absolute;left:176px;top:90px;font:700 18px/1 "Montserrat",sans-serif;color:#fff}
.contacts{position:absolute;left:176px;top:118px;list-style:none}
.contacts li{display:flex;align-items:center;gap:5px;height:13.4px;font-size:6.3px;color:#fff}
.contacts .ico{width:8px;height:8px;background:#fff;display:flex;align-items:center;justify-content:center}
</style>
</head>
<body>

<!-- 1 Cover -->
<section class="slide col-1 row-1">
  <div class="art" role="img" aria-label="Business person holding a tablet with a city skyline overlay" style="left:170px;top:0;width:186px;height:200px;background:linear-gradient(110deg,#ffffff 0%,#e6eef6 35%,#b8cde2 60%,#dbe6f1 85%,#ffffff 100%)"></div>
  <div class="brand large"><span class="mark"></span>NORDAL WORKS</div>
  <div class="cover-title">Presentation<br>title goes here</div>
  <div class="cover-sub">Lorem ipsum dolor</div>
  <div class="cover-date">Date: XX-XX-XXXX</div>
</section>

<!-- 2 Contents -->
<section class="slide col-2 row-1">
  <div class="rail"></div>
  <div class="tab t1 c-black active">1<span class="label">CONTENT</span></div>
  <div class="tab t2 c-green">2</div><div class="tab t3 c-teal">3</div><div class="tab t4 c-yellow">4</div>
  <div class="tab t5 c-red">5</div><div class="tab t6 c-olive">6</div><div class="tab t7 c-slate">7</div>
  <div class="brand small"><span class="mark"></span>NORDAL WORKS</div>
  <div class="heading" style="left:74px;top:28px">Lorem ipsum</div>
  <ol class="toc">
    <li><span class="n">1.</span>Lorem ipsum<span class="dots"></span>02</li>
    <li><span class="n">2.</span>Lorem ipsum<span class="dots"></span>05</li>
    <li><span class="n">3.</span>Lorem ipsum<span class="dots"></span>07</li>
    <li><span class="n">4.</span>Lorem ipsum<span class="dots"></span>11</li>
    <li><span class="n">5.</span>Lorem ipsum<span class="dots"></span>13</li>
    <li><span class="n">6.</span>Lorem ipsum<span class="dots"></span>16</li>
    <li><span class="n">7.</span>Lorem ipsum<span class="dots"></span>18</li>
    <li><span class="n">8.</span>Lorem ipsum<span class="dots"></span>20</li>
  </ol>
  <div class="pager"><i></i>2<i></i></div>
</section>

<!-- 3 About -->
<section class="slide col-3 row-1">
  <div class="rail"></div>
  <div class="tab t1 c-black">1</div>
  <div class="tab t2 c-green active">2<span class="label">ABOUT US</span></div>
  <div class="tab t3 c-teal">3</div><div class="tab t4 c-yellow">4</div>
  <div class="tab t5 c-red">5</div><div class="tab t6 c-olive">6</div><div class="tab t7 c-slate">7</div>
  <div class="art" role="img" aria-label="Faint world map" style="left:150px;top:28px;width:196px;height:130px;background:radial-gradient(ellipse at center,#ececec 0%,#f5f5f5 60%,#ffffff 100%)"></div>
  <div class="brand small"><span class="mark"></span>NORDAL WORKS</div>
  <div class="heading" style="left:61px;top:58px">Our company</div>
  <p class="body" style="left:61px;top:78px;width:112px">We build and support business systems for small and medium companies across the Baltic region. Our flat-rate offerings replace open-ended projects with clear scope, fixed pricing and dependable delivery. Every service is designed around simplicity, transparency and quality, so our clients can plan ahead with confidence. From ERP rollout to infrastructure care, one team stays with you from the first workshop to daily support, giving you peace of mind and a partner you can trust for years to come.</p>
  <div class="pager"><i></i>3<i></i></div>
</section>

<!-- 4 Bar chart -->
<section class="slide col-1 row-2">
  <div class="rail"></div>
  <div class="tab t1 c-black">1</div><div class="tab t2 c-green">2</div><div class="tab t3 c-teal">3</div>
  <div class="tab t4 c-yellow">4</div><div class="tab t5 c-red">5</div>
  <div class="tab t6 c-olive active">6<span class="label">BAR CHART</span></div>
  <div class="tab t7 c-slate">7</div>
  <div class="brand small"><span class="mark"></span>NORDAL WORKS</div>
  <div class="heading" style="left:74px;top:28px">Lorem ipsum</div>
  <p class="lead" style="left:74px;top:46px;width:180px">Results grew steadily each year as more clients moved to our fixed monthly service plans.</p>
  <svg class="art" style="left:68px;top:68px" width="200" height="112" viewBox="0 0 200 112" font-family="Open Sans, sans-serif" font-size="3.5" fill="#6b6e73">
    <g stroke="#e2e3e5" stroke-width=".5">
      <line x1="16" y1="6" x2="195" y2="6"/><line x1="16" y1="20.5" x2="195" y2="20.5"/>
      <line x1="16" y1="35" x2="195" y2="35"/><line x1="16" y1="49.5" x2="195" y2="49.5"/>
      <line x1="16" y1="64" x2="195" y2="64"/><line x1="16" y1="78.5" x2="195" y2="78.5"/>
    </g>
    <line x1="16" y1="93" x2="195" y2="93" stroke="#9a9ca0" stroke-width=".5"/>
    <g text-anchor="end">
      <text x="13" y="7">120</text><text x="13" y="21.5">100</text><text x="13" y="36">80</text>
      <text x="13" y="50.5">60</text><text x="13" y="65">40</text><text x="13" y="79.5">20</text><text x="13" y="94">0</text>
    </g>
    <g>
      <rect x="22" y="35" width="8" height="58" fill="#13b9b5"/><rect x="31" y="56.7" width="8" height="36.3" fill="#fcd000"/><rect x="40" y="78.5" width="8" height="14.5" fill="#0b0b0c"/>
      <rect x="63" y="78.5" width="8" height="14.5" fill="#13b9b5"/><rect x="72" y="20.5" width="8" height="72.5" fill="#fcd000"/><rect x="81" y="38.6" width="8" height="54.4" fill="#0b0b0c"/>
      <rect x="104" y="49.5" width="8" height="43.5" fill="#13b9b5"/><rect x="113" y="49.5" width="8" height="43.5" fill="#fcd000"/><rect x="122" y="67.6" width="8" height="25.4" fill="#0b0b0c"/>
      <rect x="145" y="56.7" width="8" height="36.3" fill="#13b9b5"/><rect x="154" y="78.5" width="8" height="14.5" fill="#fcd000"/><rect x="163" y="31.4" width="8" height="61.6" fill="#0b0b0c"/>
    </g>
    <g text-anchor="middle"><text x="35" y="100">2010</text><text x="76" y="100">2011</text><text x="117" y="100">2012</text><text x="158" y="100">2013</text></g>
    <g><rect x="60" y="104" width="3" height="3" fill="#13b9b5"/><text x="64" y="107">Tablet</text>
      <rect x="78" y="104" width="3" height="3" fill="#fcd000"/><text x="82" y="107">Phone</text>
      <rect x="95" y="104" width="3" height="3" fill="#0b0b0c"/><text x="99" y="107">Device</text></g>
  </svg>
  <div style="position:absolute;left:262px;top:76px;font-size:5px;font-weight:600;color:var(--ink)">Lorem ipsum</div>
  <p class="body" style="left:262px;top:86px;width:60px;color:#333">Tablet sales led in the first year, then phones took over as mobile work became common for our clients and their teams.</p>
  <p class="body" style="left:262px;top:136px;width:60px;color:#333">Device orders climbed fast in the last year with new field service plans.</p>
  <div class="pager"><i></i>12<i></i></div>
</section>

<!-- 5 Highlight stat -->
<section class="slide col-2 row-2">
  <div class="rail"></div>
  <div class="tab t1 c-black" style="width:52px">1</div>
  <div class="tab t2 c-green">2</div><div class="tab t3 c-teal">3</div><div class="tab t4 c-yellow">4</div>
  <div class="tab t5 c-red">5</div><div class="tab t6 c-olive">6</div><div class="tab t7 c-slate">7</div>
  <div class="art" role="img" aria-label="Cloud of small app and service icons" style="left:196px;top:0;width:160px;height:78px;background:radial-gradient(ellipse at 65% 30%,#cfd1d4 0%,#e8e9eb 45%,#ffffff 80%)"></div>
  <div class="heading" style="left:74px;top:28px">Lorem ipsum</div>
  <p class="body" style="left:61px;top:54px;width:72px">Our monthly plans bundle licences, hosting and support in one clear price. You always know what you pay for and what you receive in return.</p>
  <p class="body" style="left:143px;top:54px;width:72px">Standard packages make it easy to start small and grow. Add users, modules or locations whenever your business needs more capacity.</p>
  <div class="stat-band"></div>
  <div class="stat-num">91<sup>%</sup></div>
  <p class="stat-text">of clients renew their service plan, citing clear pricing and fast, friendly support as main reasons.</p>
  <div class="art" role="img" aria-label="Three smartphones of different sizes" style="left:236px;top:82px;width:92px;height:102px;background:linear-gradient(180deg,#f2f2f2,#d6d7d9)"></div>
  <div class="pager"><i></i>5<i></i></div>
</section>

<!-- 6 Timeline -->
<section class="slide col-3 row-2">
  <div class="rail"></div>
  <div class="tab t1 c-black">1</div><div class="tab t2 c-green">2</div>
  <div class="tab t3 c-teal active">3<span class="label">ABOUT US</span></div>
  <div class="tab t4 c-yellow">4</div><div class="tab t5 c-red">5</div><div class="tab t6 c-olive">6</div><div class="tab t7 c-slate">7</div>
  <div class="brand small"><span class="mark"></span>NORDAL WORKS</div>
  <div class="heading" style="left:74px;top:28px">Timeline</div>
  <div class="tl-line"></div>
  <div class="tl-year" style="left:195px;top:30px;color:var(--violet)">1998-2000</div>
  <p class="tl-text" style="left:195px;top:38px">The company starts with a small team installing office networks and servers for local firms.</p>
  <div class="tl-year" style="left:136px;top:68px;color:var(--magenta)">2000-2003</div>
  <p class="tl-text r" style="left:94px;top:76px">First ERP projects delivered for trade and logistics clients, with a dedicated support desk.</p>
  <div class="tl-year" style="left:195px;top:106px;color:var(--olive)">2003-2005</div>
  <p class="tl-text" style="left:195px;top:114px">A second office opens and the team doubles to meet growing demand for managed services.</p>
  <div class="tl-year" style="left:136px;top:145px;color:var(--green)">2005-2006</div>
  <p class="tl-text r" style="left:94px;top:153px">Cloud hosting and remote monitoring join the offer, keeping client systems safe around the clock.</p>
  <div class="pager"><i></i>4<i></i></div>
</section>

<!-- 7-9 Section dividers -->
<section class="slide col-1 row-3 section bg-black">
  <div class="art" role="img" aria-label="Connected dots network pattern" style="left:180px;top:0;width:176px;height:200px;background:radial-gradient(ellipse at 80% 30%,rgba(255,255,255,.10),rgba(255,255,255,0) 70%)"></div>
  <div class="sec-title">SECTION</div>
  <p class="sec-text">This part covers our standard offerings, how each plan is built, what it includes and how clients move from a first meeting to a running system with fixed monthly fees and clear service levels for every user.</p>
</section>
<section class="slide col-2 row-3 section bg-green">
  <div class="art" role="img" aria-label="Connected dots network pattern" style="left:180px;top:0;width:176px;height:200px;background:radial-gradient(ellipse at 80% 30%,rgba(255,255,255,.18),rgba(255,255,255,0) 70%)"></div>
  <div class="sec-title">SECTION</div>
  <p class="sec-text">This part covers our standard offerings, how each plan is built, what it includes and how clients move from a first meeting to a running system with fixed monthly fees and clear service levels for every user.</p>
</section>
<section class="slide col-3 row-3 section bg-teal">
  <div class="art" role="img" aria-label="Connected dots network pattern" style="left:180px;top:0;width:176px;height:200px;background:radial-gradient(ellipse at 80% 30%,rgba(255,255,255,.18),rgba(255,255,255,0) 70%)"></div>
  <div class="sec-title">SECTION</div>
  <p class="sec-text">This part covers our standard offerings, how each plan is built, what it includes and how clients move from a first meeting to a running system with fixed monthly fees and clear service levels for every user.</p>
</section>

<!-- 10 Services -->
<section class="slide col-1 row-4">
  <div class="rail"></div>
  <div class="tab t1 c-black">1</div><div class="tab t2 c-green">2</div><div class="tab t3 c-teal">3</div><div class="tab t4 c-yellow">4</div>
  <div class="tab t5 c-red active">5<span class="label">OUR SERVICE</span></div>
  <div class="tab t6 c-olive">6</div><div class="tab t7 c-slate">7</div>
  <div class="brand small"><span class="mark"></span>NORDAL WORKS</div>
  <div class="heading" style="left:74px;top:28px">What we do</div>
  <div class="service" style="left:68px;top:66px"><div class="icon c-teal"><svg width="12" height="10" viewBox="0 0 12 10"><rect x="1.5" y="1" width="9" height="6" fill="none" stroke="#fff"/><rect x="0" y="8" width="12" height="1.2" fill="#fff"/></svg></div><div class="name">Lorem ipsum</div><p class="txt">Workstations set up, updated and kept running for every team member.</p></div>
  <div class="service" style="left:201px;top:66px"><div class="icon c-green"><svg width="12" height="10" viewBox="0 0 12 10"><rect x="0.5" y="0.5" width="9" height="7" fill="none" stroke="#fff"/><rect x="3" y="3" width="8.5" height="6.5" fill="#fff"/></svg></div><div class="name">Lorem ipsum</div><p class="txt">Shared documents and files stored safely with daily backups.</p></div>
  <div class="service" style="left:68px;top:104px"><div class="icon c-teal"><svg width="12" height="10" viewBox="0 0 12 10"><path d="M1 9V1M1 9h10M3 7l2.5-3 2 2L11 2v5z" fill="#fff" stroke="#fff" stroke-width=".8"/></svg></div><div class="name">Lorem ipsum</div><p class="txt">Clear reports on sales, stock and finance straight from your ERP.</p></div>
  <div class="service" style="left:201px;top:104px"><div class="icon c-green"><svg width="12" height="10" viewBox="0 0 12 10"><rect x="3" y="0.5" width="6" height="3" fill="#fff"/><rect x="0.5" y="3.5" width="11" height="4" fill="#fff"/><rect x="3" y="6" width="6" height="3.5" fill="#fff" stroke="#8dc63f" stroke-width=".5"/></svg></div><div class="name">Lorem ipsum</div><p class="txt">Printers and office devices managed as part of one plan.</p></div>
  <div class="service" style="left:68px;top:142px"><div class="icon c-teal"><svg width="12" height="10" viewBox="0 0 12 10"><rect x="0.5" y="2" width="11" height="7.5" rx="1" fill="#fff"/><rect x="4" y="0.5" width="4" height="2" fill="#fff"/><circle cx="6" cy="5.7" r="2.2" fill="#13b9b5"/></svg></div><div class="name">Lorem ipsum</div><p class="txt">Security and access control to keep your premises protected.</p></div>
  <div class="service" style="left:201px;top:142px"><div class="icon c-green"><svg width="12" height="10" viewBox="0 0 12 10"><circle cx="6" cy="2.8" r="2.3" fill="#fff"/><path d="M1.5 10c0-3 2-4.5 4.5-4.5S10.5 7 10.5 10z" fill="#fff"/></svg></div><div class="name">Lorem ipsum</div><p class="txt">Training and a named contact person for each of your users.</p></div>
  <div class="pager"><i></i>11<i></i></div>
</section>

<!-- 11 Team of four -->
<section class="slide col-2 row-4">
  <div class="rail"></div>
  <div class="tab t1 c-black">1</div><div class="tab t2 c-green">2</div><div class="tab t3 c-teal">3</div>
  <div class="tab t4 c-yellow active">4<span class="label">OUR TEAM</span></div>
  <div class="tab t5 c-red">5</div><div class="tab t6 c-olive">6</div><div class="tab t7 c-slate">7</div>
  <div class="brand small"><span class="mark"></span>NORDAL WORKS</div>
  <div class="heading" style="left:74px;top:28px;line-height:1.45">Lorem<br>ipsum dolor</div>
  <div class="portrait" role="img" aria-label="Portrait photo of a team member" style="left:75px;top:65px"></div>
  <div class="portrait" role="img" aria-label="Portrait photo of a team member" style="left:134px;top:65px"></div>
  <div class="portrait" role="img" aria-label="Portrait photo of a team member" style="left:197px;top:65px"></div>
  <div class="portrait" role="img" aria-label="Portrait photo of a team member" style="left:259px;top:65px"></div>
  <div class="member" style="left:70px;top:117px"><div class="who">LOREM IPSUM</div><div class="role">Lorem ipsum</div><p class="bio">Leads ERP rollouts and keeps every project on time and on budget for our clients.</p></div>
  <div class="member" style="left:129px;top:117px"><div class="who">LOREM IPSUM</div><div class="role">Lorem ipsum</div><p class="bio">Designs network and server setups that stay simple, safe and easy to grow.</p></div>
  <div class="member" style="left:192px;top:117px"><div class="who">LOREM IPSUM</div><div class="role">Lorem ipsum</div><p class="bio">Runs the support desk and makes sure every request gets a fast answer.</p></div>
  <div class="member" style="left:254px;top:117px"><div class="who">LOREM IPSUM</div><div class="role">Lorem ipsum</div><p class="bio">Guides new clients through plans, pricing and the first weeks of service.</p></div>
  <div class="pager"><i></i>10<i></i></div>
</section>

<!-- 12 Team of five -->
<section class="slide col-3 row-4">
  <div class="rail"></div>
  <div class="tab t1 c-black">1</div><div class="tab t2 c-green">2</div><div class="tab t3 c-teal">3</div>
  <div class="tab t4 c-yellow active">4<span class="label">OUR TEAM</span></div>
  <div class="tab t5 c-red">5</div><div class="tab t6 c-olive">6</div><div class="tab t7 c-slate">7</div>
  <div class="brand small"><span class="mark"></span>NORDAL WORKS</div>
  <div class="heading" style="left:74px;top:28px;line-height:1.45">Lorem<br>ipsum dolor<br>sit amet</div>
  <div class="portrait" role="img" aria-label="Portrait photo of a team member" style="left:153px;top:24px;width:60px;height:59px"></div>
  <div class="portrait" role="img" aria-label="Portrait photo of a team member" style="left:240px;top:24px;width:60px;height:59px"></div>
  <div class="portrait" role="img" aria-label="Portrait photo of a team member" style="left:66px;top:114px;width:60px;height:59px"></div>
  <div class="portrait" role="img" aria-label="Portrait photo of a team member" style="left:153px;top:114px;width:60px;height:59px"></div>
  <div class="portrait" role="img" aria-label="Portrait photo of a team member" style="left:240px;top:114px;width:60px;height:59px"></div>
  <div class="member" style="left:155px;top:86px"><div class="who">LOREM IPSUM</div><div class="role">Lorem ipsum</div></div>
  <div class="member" style="left:242px;top:86px"><div class="who">LOREM IPSUM</div><div class="role">Lorem ipsum</div></div>
  <div class="member" style="left:68px;top:176px"><div class="who">LOREM IPSUM</div><div class="role">Lorem ipsum</div></div>
  <div class="member" style="left:155px;top:176px"><div class="who">LOREM IPSUM</div><div class="role">Lorem ipsum</div></div>
  <div class="member" style="left:242px;top:176px"><div class="who">LOREM IPSUM</div><div class="role">Lorem ipsum</div></div>
  <div class="pager"><i></i>9<i></i></div>
</section>

<!-- 13 Orders table -->
<section class="slide col-1 row-5">
  <div class="rail"></div>
  <div class="tab t1 c-black">1</div><div class="tab t2 c-green">2</div><div class="tab t3 c-teal">3</div>
  <div class="tab t4 c-yellow">4</div><div class="tab t5 c-red">5</div><div class="tab t6 c-olive">6</div>
  <div class="tab t7 c-slate active">7<span class="label">TABLE</span></div>
  <div class="brand small"><span class="mark"></span>NORDAL WORKS</div>
  <div class="heading" style="left:74px;top:28px">Lorem ipsum</div>
  <p class="lead" style="left:74px;top:46px;width:180px">A short summary of recent orders placed through the new monthly service plans.</p>
  <table class="orders">
    <tr><th>Name</th><th>Order</th><th>Amount</th><th>Description</th></tr>
    <tr><td>Anna Ozola</td><td>Server care plan</td><td>50 pcs</td><td>Yearly renewal</td></tr>
    <tr><td>Juris Kalns</td><td>Office network</td><td>20 pcs</td><td>New branch</td></tr>
    <tr><td>Ilze Berga</td><td>ERP starter pack</td><td>35 pcs</td><td>First rollout</td></tr>
    <tr><td>Peteris Liepa</td><td>Backup service</td><td>40 pcs</td><td>Added users</td></tr>
    <tr><td>Marta Egle</td><td>Support desk plan</td><td>75 pcs</td><td>Upgrade</td></tr>
  </table>
  <div class="pager"><i></i>13<i></i></div>
</section>

<!-- 14 Ledger table -->
<section class="slide col-2 row-5">
  <div class="rail"></div>
  <div class="tab t1 c-violet">1</div><div class="tab t2 c-magenta">2</div><div class="tab t3 c-red">3</div>
  <div class="tab t4 c-red" style="background:#e4572e">4</div><div class="tab t5 c-yellow" style="background:#f2a900">5</div>
  <div class="tab t6 c-green">6</div>
  <div class="tab t7 c-slate active">7<span class="label">BAR CHART</span></div>
  <div class="brand small"><span class="mark"></span>NORDAL WORKS</div>
  <div class="heading" style="left:74px;top:28px">Lorem ipsum</div>
  <p class="lead" style="left:74px;top:44px;width:180px">A simple view of plan costs per item, showing how each part adds up to one total.</p>
  <table class="ledger">
    <tr><th style="width:124px">Lorem ipsum</th><th style="width:59px;text-align:center">$</th><th style="text-align:center">$</th></tr>
    <tr><td>Lorem ipsum</td><td></td><td class="v">00000</td></tr>
    <tr><td>Lorem ipsum</td><td></td><td class="v">00000</td></tr>
    <tr><td class="in">Lorem ipsum</td><td class="v">00000</td><td></td></tr>
    <tr><td class="in">Lorem ipsum</td><td class="v">00000</td><td></td></tr>
    <tr><td>Indoor placements</td><td></td><td class="v">00000</td></tr>
    <tr><td class="in">Lorem ipsum</td><td class="v">00000</td><td></td></tr>
    <tr><td class="in">Lorem ipsum</td><td class="v">00000</td><td></td></tr>
    <tr><td>Lorem ipsum</td><td></td><td class="v">00000</td></tr>
    <tr class="total"><td>Total</td><td></td><td class="v" style="color:#fff">00000</td></tr>
  </table>
  <div class="pager"><i></i>14<i></i></div>
</section>

<!-- 15 Closing -->
<section class="slide col-3 row-5 bg-black" style="background:var(--black)">
  <div class="art" role="img" aria-label="Connected dots network pattern" style="left:0;top:0;width:180px;height:200px;background:radial-gradient(ellipse at 30% 50%,rgba(255,255,255,.10),rgba(255,255,255,0) 70%)"></div>
  <div class="thanks">Thank You !</div>
  <ul class="contacts">
    <li><span class="ico"><svg width="6" height="6" viewBox="0 0 6 6"><path d="M1 .5l1.2 1.3-.6.9c.4.8 1 1.4 1.8 1.8l.9-.6L5.5 5 4.8 5.6C2.5 5.3.7 3.5.4 1.2z" fill="#0b0b0c"/></svg></span>000.000.0000</li>
    <li><span class="ico"><svg width="6" height="6" viewBox="0 0 6 6"><circle cx="3" cy="3" r="2.5" fill="none" stroke="#0b0b0c" stroke-width=".6"/><path d="M.5 3h5M3 .5c-1.5 1.5-1.5 3.5 0 5M3 .5c1.5 1.5 1.5 3.5 0 5" fill="none" stroke="#0b0b0c" stroke-width=".5"/></svg></span>www.yourwebsite.com</li>
    <li><span class="ico" style="font:700 6px/1 'Open Sans',sans-serif;color:#0b0b0c">@</span>info@yourwebsite.com</li>
    <li><span class="ico"></span>@yourwebsite</li>
    <li><span class="ico"></span>socialnet.com/ yourwebsite</li>
  </ul>
</section>

</body>
</html>
```